(Wordpress)Website Design - No requirements! Sign Your name at the bottom of the site!

Dear Designer,

I am looking for a designer who is interested in a long-term business realtionship.
I already have 2 more designs to get done IMMEDIATELY after this website..
1.) An email brochure matching the website theme.
2.) A Billboard. BOTH MATCHING THE WEBSITE THEME

For this project, a bonus WILL be given.

Go to vaultmoor.com as Site Inspiration

Please take this opportunity to design an existing wordpress website, FUNDSWIFTLANE.com, in whatever form your creativity takes you

I have no requirements other than a CREATIVE and OUT-OF -THE-BOX Design. Something Pretty and Eye Catching; a website that someone logs onto and doesnt want to leave

I have purchased a theme called lumetra. You dont need to use it...But Info can be found at

http://skinbazaar.example/item/lumetra-premium-wordpress-theme/full_screen_preview/572046

I have attached my logos and a PDF with a short story about what our company does.

Thank You,
-Tobin
PS I HAVE ANOTHER 2 DESIGNS TO DO AFTER THIS PROJECT.
also, IF YOU KNOW OF SOMEONE WHO DOES SEO WORK, I AM LOOKING FOR A FULL-TIME EMPLOYEE

Target Market(s)

Business Owners in a state of finacial NEED

Industry/Entity Type

Business

Requirements
Must have
• COLORFUL, EYE CATCHING

```html
<!DOCTYPE html>
<html lang="en">
<head>
<meta charset="utf-8">
<title>Swiftlane Capital</title>
<link rel="stylesheet" href="https://fonts.googleapis.com/css2?family=Comfortaa:wght@400;700&family=PT+Sans:wght@400;700&family=Arimo:wght@400;700&display=swap">
<style>
:root{
  --paper:#f1ebe8;
  --paper-light:#f5f0ee;
  --paper-dark:#ebe3e0;
  --ink:#2b2b2b;
  --ink-soft:#4a4a4a;
  --hero:#b0b1b3;
  --hero-line:#d9d9d9;
  --white:#ffffff;
  --brand-blue:#2f6fb8;
  --btn-top:#6cc4fb;
  --btn-bottom:#1a8ef0;
  --btn-frame:#8a8b8d;
  --accent:#e5520c;
  --dot:#8d8d8d;
  --divider:#d6d0cc;
}
*{margin:0;padding:0;box-sizing:border-box}
html,body{width:1200px;height:1059px;overflow:hidden;background:var(--paper)}
.page{position:relative;width:1200px;height:1059px;font-family:'Arimo',sans-serif;color:var(--ink)}
.paper-bg{position:absolute;inset:0;background:radial-gradient(ellipse at 30% 40%,var(--paper-light) 0%,var(--paper) 55%,var(--paper-dark) 100%)}

.site-header{position:absolute;left:0;top:0;width:1200px;height:81px}
.brand{position:absolute;left:78px;top:18px;display:flex;align-items:center;gap:10px}
.brand-mark{width:40px;height:40px;border-radius:50%;background:var(--brand-blue)}
.brand-name{font-family:'PT Sans',sans-serif;font-weight:400;font-size:38px;color:var(--brand-blue);letter-spacing:-0.5px}

.main-nav{position:absolute;left:513px;top:20px;display:flex;height:48px}
.main-nav a{display:flex;align-items:center;padding:0 18px;font-size:15px;color:var(--ink);text-decoration:none;border-right:1px solid var(--divider)}
.main-nav a:last-child{border-right:none}

.call-us{position:absolute;left:982px;top:0;width:155px;height:94px}
.call-us svg{position:absolute;left:0;top:0}
.call-us .call-label{position:absolute;width:100%;top:10px;text-align:center;font-family:'PT Sans',sans-serif;font-size:23px;color:var(--white);letter-spacing:.5px}
.call-us .call-phone{position:absolute;width:100%;top:46px;text-align:center;font-size:17px;color:var(--white)}

.hero{position:absolute;left:0;top:81px;width:1200px;height:477px;background:var(--hero);border-bottom:3px solid var(--hero-line)}
.hero-photo{position:absolute;left:242px;top:0;width:622px;height:474px;background:radial-gradient(ellipse at 60% 70%,#c4c5c7 0%,#b3b4b6 55%,var(--hero) 100%)}
.hero-title{position:absolute;left:0;width:1200px;top:76px;text-align:center;font-family:'Comfortaa',sans-serif;font-weight:400;font-size:42px;color:var(--white);letter-spacing:.3px}
.hero-copy{position:absolute;left:294px;top:160px;width:620px;font-family:'PT Sans',sans-serif;font-size:31px;line-height:38px;color:var(--white);letter-spacing:.6px}
.hero-cta-frame{position:absolute;left:437px;top:358px;width:317px;height:91px;background:var(--btn-frame);border-radius:6px;opacity:.9}
.hero-cta{position:absolute;left:459px;top:375px;width:274px;height:58px;border-radius:5px;background:linear-gradient(var(--btn-top),var(--btn-bottom));display:flex;align-items:center;justify-content:center;font-family:'PT Sans',sans-serif;font-size:39px;color:var(--white);text-decoration:none}

.slider-dots{position:absolute;left:570px;top:574px;display:flex;gap:10px}
.slider-dots span{width:9px;height:9px;border-radius:50%;background:var(--dot)}
.slider-dots span.active{background:var(--accent)}

.scroll-down{position:absolute;left:577px;top:594px}
.section-line{position:absolute;left:605px;top:661px;height:176px;border-left:1px dashed var(--ink)}

.section-heading{position:absolute;left:0;top:840px;width:1200px;height:160px;text-align:center}
.section-heading .pre{position:absolute;left:0;width:1200px;top:0;font-family:'Comfortaa',sans-serif;font-size:17px;color:var(--ink-soft)}
.section-heading .ribbon{position:absolute;left:517px;top:22px;width:177px;height:68px;background:var(--accent)}
.section-heading .ribbon-label{position:absolute;left:517px;top:22px;width:177px;height:68px;display:flex;align-items:center;justify-content:center;font-family:'Comfortaa',sans-serif;font-size:22px;color:var(--white);letter-spacing:1.5px}
.section-heading .mid{position:absolute;left:0;width:1200px;top:92px;font-family:'Comfortaa',sans-serif;font-size:16px;color:var(--ink-soft)}
.section-heading .main{position:absolute;left:0;width:1200px;top:108px;font-family:'Arimo',sans-serif;font-weight:700;font-size:37px;color:var(--ink-soft)}
</style>
</head>
<body>
<div class="page">
  <div class="paper-bg" role="img" aria-label="Soft recycled paper texture background"></div>

  <header class="site-header">
    <div class="brand">
      <span class="brand-mark"></span>
      <span class="brand-name">Swiftlane Capital</span>
    </div>
    <nav class="main-nav">
      <a href="#">About</a>
      <a href="#">Success Stories</a>
      <a href="#">Apply</a>
      <a href="#">Swiftlane Charity</a>
    </nav>
    <div class="call-us">
      <svg width="155" height="94" viewBox="0 0 155 94">
        <defs>
          <linearGradient id="callFill" x1="0" y1="0" x2="0" y2="1">
            <stop offset="0" stop-color="#3aa4e4"/>
            <stop offset="1" stop-color="#2a86cc"/>
          </linearGradient>
        </defs>
        <polygon points="0,0 155,0 155,86 0,94" fill="url(#callFill)"/>
      </svg>
      <div class="call-label">CALL US</div>
      <div class="call-phone">(555) 014-2290</div>
    </div>
  </header>

  <section class="hero">
    <div class="hero-photo" role="img" aria-label="Photo of rising stacks of silver coins"></div>
    <h1 class="hero-title">Welcome to Swiftlane Capital</h1>
    <p class="hero-copy">We are a funding agency helping business like you get the money they need.<br>We go above and beyond searhing for the best deal for you.</p>
    <div class="hero-cta-frame"></div>
    <a class="hero-cta" href="#">About</a>
  </section>

  <div class="slider-dots"><span></span><span></span><span class="active"></span><span></span></div>

  <svg class="scroll-down" width="56" height="56" viewBox="0 0 56 56">
    <circle cx="28" cy="28" r="27" fill="#ffffff"/>
    <circle cx="28" cy="28" r="23" fill="#f07d10"/>
    <circle cx="28" cy="28" r="18" fill="#ffffff"/>
    <circle cx="28" cy="28" r="15" fill="#f26b0e"/>
    <polygon points="24,17 32,17 32,27 37,27 28,38 19,27 24,27" fill="#ffffff"/>
  </svg>
  <div class="section-line"></div>

  <div class="section-heading">
    <span class="pre">The</span>
    <div class="ribbon" role="img" aria-label="Orange ribbon banner behind the word Dilemma"></div>
    <span class="ribbon-label">DILEMMA</span>
    <span class="mid">We Are</span>
    <span class="main">Facing</span>
  </div>
</div>
</body>
</html>
```